Web Design Project: Need three pages designed, all for same site

Hello,

I am creating a new website that needs a clean, professional look. I need three of the pages designed for the site- all three will have the same header and footer, same brand, same top menu. These three pages represent three unique pages and unique functionality that will allow me to map out the website and then come back here and post a job for the rest of the pages.

The three pages are the Home page, the Profile Page, and the Results page.

I want an extremely simple design for these pages- my goal is for these pages to be rendered almost entirely in "code" with absolute minimal graphics- so use square corners instead of rounded ones, and simple graphic design elements that can be encoded are required.

I need a completely uncompressed PSD file of each of these pages. I want a fixed width site, with some sort of background that looks like a slight gradient up to the edge of the site to make a nice impact on the screen- look at www.plorvex.net for an example of what I am talking about. Also- the visible page should be the same width as that site.

Besides the background edge gradient framing the outside of the site, I would prefer if the only graphical elements are the site logo and a couple of small open-source icons for email and expansion with a "plus" symbol. A background image may be alright if the design is really good and the image is small so it can be quickly loaded.

I want very clean design, very simple. I will have these pages converted to HTML by a separate group.

One Bar Ad Placeholder should be located on every page in a common placement at the top- 728 by 90

Links that should be included in the main navigation bar at the top of the pages:

1. Home
2. About Us
3. Attorney Information
4. Medical Providers- Click Here To List Your Office For Free!

The Medical Providers link should be made to stand out- that is the call to action for medical providers to sign up on the site.

Other links that should be accounted for on all pages:

Login button
Username: (input field)
Password: (input field)
Forgot Login Info?
Create Account
Contact Us
Privacy Policy
Quillbook Like
Zarnix +
Hooked-Up logo
Chirpel

Requirements for each individual page:

Home Page:

This will be the home page for the site. It will contain all of the links off of it for the main site menu and navigation elements placed here will appear throughout the site. It will also have a login function at the top right and a logo in the top left.

It will have a search function dominating the left side of the home page consisting of two search input areas:

1. An open search field bar with a Sentence "Open Search by Category and city, or Provider Name: (search input field)"

2. A search panel with address, city, state, zip and two categories of drop down search screening.

The right side of the page will have a placeholder for a vidmora introduction video and some basic instructions above and below it.

Essentially, the home page is an introduction to the site and an immediate call to action to use the site for what it is intended to be used for- searching for doctors.

Profile Page:

This will be a page that is used to show the profile of the provider that has been selected. This page must be a format that can be used with all providers listed, no matter how much information each chooses to list. I want a clean appearance and placeholder text will be used to show the placement of various elements on the page. This page will be automatically generated by each provider's information with the same layout for all providers. The information included in the design should be:

Logo
Office name and specialty
Location addresses
Billing Address
Photographs of doctors with their name and specialty
Review average with number of reviews, date of oldest review, and average rating.
Individual Reviews with star rating and synopsis

Results Page:

This is a grid to display four account types as they will be listed- simple page-wide results bars displaying listings, like any search-results driven site. Each result will be clickable to expand it and show more information, so each entry on the page will need to be designed both as closed and the open panel position showing more information. Each result will build on the lesser one before it. This design will be converted to a grid that will be rendered in code, so they should be fairly simple.

That's it.

I am not looking for some complex design, or some loud website layout. I want a simple, functional, clean and professional website for my company. I will want this design to be converted to HTML code, so remember- use fonts that are common to the web. Professional, clean layout is the key here.

I will attach a logo file that you can download in AI 4 format. I do not want it altered.

I will also attach a list of menu items for the menu bar and links that will need to be on every page. For now, simply use placeholder words for them.

I added the links and menu items I need on all pages to make the top navigation and bottom footer.  

Target Market(s)

Attorneys and their clients

Industry/Entity Type

Graphic Design

Requirements
Must have
• Clear usability

```html
<!DOCTYPE html>
<html lang="en">
<head>
<meta charset="utf-8">
<title>TrevaloCare – Home</title>
<link rel="stylesheet" href="https://fonts.googleapis.com/css2?family=Roboto:wght@300;400;500;700&display=swap">
<style>
:root{
  --brand-blue:#1f62ab;
  --brand-blue-dark:#1b4f8c;
  --headline-blue:#2f74b8;
  --navy:#1b2c55;
  --text:#2b2b2b;
  --muted:#8a8a8a;
  --panel:#ebebeb;
  --field-border:#d6d6d6;
  --line:#d9d9d9;
  --edge-grey:#d7d7d7;
  --white:#ffffff;
  --ad-link:#1a0dab;
  --ad-url:#1f8f1f;
}
*{box-sizing:border-box;margin:0;padding:0}
html,body{width:1200px;height:800px;overflow:hidden}
body{
  font-family:"Roboto",Arial,sans-serif;color:var(--text);position:relative;
  background:linear-gradient(90deg,#fff 0,var(--edge-grey) 12%,#e2e2e2 16%,#e2e2e2 84%,var(--edge-grey) 88%,#fff 100%);
}
.abs{position:absolute}
.site-header{left:192px;top:0;width:816px;height:104px;background:var(--white)}
.ad-band{left:192px;top:104px;width:816px;height:88px}
.page{left:192px;top:192px;width:816px;height:608px;background:var(--white)}

.login-field{height:23px;border:1px solid var(--field-border);background:#fff;font-size:10px;color:var(--muted);padding:6px 14px}
.login-btn{left:792px;top:6px;width:32px;height:23px;background:#a9a9a9}
.util-link{top:12px;font-size:9px;color:#444}

.brand{left:224px;top:44px;font-size:30px;font-weight:400;color:var(--navy);letter-spacing:-.5px}
.nav-link{top:60px;font-size:13px;color:#222}
.nav-active-bar{left:456px;top:45px;width:35px;height:2px;background:var(--brand-blue)}
.nav-cta{color:var(--brand-blue)}
.nav-cta .free{color:#222}
.star{color:var(--brand-blue);font-size:13px;position:absolute;top:-8px;left:-8px}

.ad-box{left:308px;top:112px;width:582px;height:72px;background:#fff;border:1px solid #3a6fc4;font-size:9.5px;padding:2px 5px;line-height:13.5px}
.ad-box a{color:var(--ad-link);font-weight:700;text-decoration:underline}
.ad-box .url{color:var(--ad-url);font-size:8px}
.ad-arrows{left:310px;top:170px;width:28px;height:12px;display:flex;gap:4px}
.ad-arrows span{width:12px;height:12px;background:#9bb6dc}
.ad-arrows span+span{background:var(--brand-blue-dark)}
.ad-picks{left:821px;top:170px;width:68px;height:13px;background:var(--brand-blue);color:#fff;font-size:8.5px;padding:1px 8px}
.ad-label{left:900px;top:173px;font-size:8.5px;color:var(--muted);border-bottom:1px solid var(--muted)}

.social{top:202px;height:16px;display:flex;align-items:center;font-size:8.5px}
.social .btn{height:16px;border:1px solid #b9c2cf;background:#eef1f5;padding:2px 5px;font-weight:700;color:#333}
.social .count{height:16px;border:1px solid #c9c9c9;margin-left:4px;padding:2px 4px;color:#333;background:#fff}

.headline{left:192px;top:243px;width:816px;text-align:center;font-size:19px;font-weight:300;color:var(--headline-blue);line-height:23px}

.search-panel{left:224px;top:311px;width:496px;height:340px;background:var(--panel)}
.panel-title{font-size:14.5px;font-weight:500;color:var(--brand-blue)}
.field{background:#fff;border:1px solid var(--field-border);font-size:12px;color:#666;padding:0 15px;display:flex;align-items:center;justify-content:space-between}
.field .caret{border-left:1px solid var(--field-border);height:100%;width:30px;display:flex;align-items:center;justify-content:center;color:var(--brand-blue);font-size:9px;margin-right:-15px}
.search-btn{display:flex;align-items:center;justify-content:center}
.panel-divider{left:224px;top:405px;width:496px;height:3px;background:#fff}

.howto{left:736px;top:311px;width:240px;height:380px;border:1px solid var(--line);background:#fff}
.howto-title{font-size:14.5px;font-weight:500;color:var(--brand-blue);line-height:17px}
.howto-text{font-size:9.3px;line-height:11.5px;color:#222;width:205px}
.read-more{left:900px;top:476px;font-size:9px;font-style:italic;color:#777}
.howto-rule{left:753px;top:407px;width:206px;height:1px;background:var(--line)}
.video{left:753px;top:551px;width:205px;height:126px;background:#000}
.video-bar{left:753px;top:665px;width:205px;height:12px;background:#e6e6e6}
.video-progress{left:768px;top:670px;width:130px;height:2px;background:#777}
.video-progress-played{left:768px;top:670px;width:30px;height:2px;background:#c8302a}
.video-brand{left:914px;top:650px;font-size:10px;color:#fff}

.footer-link{top:736px;font-size:10px;color:var(--muted)}
.footer-cta{color:var(--brand-blue)}
.footer-cta .free{color:#222}
.footer-rule{left:208px;top:754px;width:784px;height:1px;background:var(--line)}
.footer-active{left:846px;top:752px;width:61px;height:2px;background:var(--brand-blue)}
</style>
</head>
<body>

<div class="abs site-header"></div>
<div class="abs ad-band"></div>
<div class="abs page"></div>

<!-- login -->
<div class="abs login-field" style="left:568px;top:6px;width:104px">Name</div>
<div class="abs login-field" style="left:680px;top:6px;width:104px">Password</div>
<div class="abs login-btn">
  <svg width="32" height="23" viewBox="0 0 32 23"><rect x="11" y="10" width="10" height="8" fill="#1f62ab"/><path d="M13 10V7a3 3 0 0 1 6 0" stroke="#1f62ab" stroke-width="1.6" fill="none"/></svg>
</div>
<span class="abs util-link" style="left:838px">Forgot Login info?</span>
<span class="abs util-link" style="left:921px">Create account</span>

<!-- brand + nav -->
<div class="abs brand">TrevaloCare</div>
<div class="abs nav-active-bar"></div>
<span class="abs nav-link" style="left:456px">Home</span>
<span class="abs nav-link" style="left:516px">About Us</span>
<span class="abs nav-link" style="left:595px">Attorney Information</span>
<span class="abs nav-link nav-cta" style="left:738px"><span class="star">*</span>Medical Providers - List Your Office <span class="free">for Free!</span></span>

<!-- ad -->
<div class="abs ad-box">
  <div><a>Affordable Hotels</a> Special rates until the end of the month. No booking fees, book your room now! <span class="url">www.example.com</span></div>
  <div><a>Dublin Hotels</a> Browse hundreds of hotels in Dublin, sort by price, location and user reviews. <span class="url">www.example.com</span></div>
  <div><a>Hotels in Ireland</a> Compare prices of 1000s of hotels all over ireland. Offers start from €100 for 2 nights! <span class="url">www.example.com</span></div>
  <div><a>Hotels</a> Great weekend offers for hotels in Dublin. Hundreds of hotels to choose from. <span class="url">www.example.com</span></div>
</div>
<div class="abs ad-arrows"><span></span><span></span></div>
<div class="abs ad-picks">AdPicks ▷</div>
<span class="abs ad-label">advertisement</span>

<!-- social -->
<div class="abs social" style="left:570px"><span class="btn">Quillbook Like</span><span class="count">15k</span></div>
<div class="abs social" style="left:650px"><span class="btn">Chirpel @plorvex</span><span class="count">28K followers</span></div>
<div class="abs social" style="left:808px"><span class="btn">Zarnix +1</span><span class="count">203</span></div>
<div class="abs social" style="left:883px"><span class="btn">Hooked-Up</span><span class="count">3,102</span></div>

<h1 class="abs headline" style="font-weight:300">TrevaloCare is the Nationwide Online Directory Of Doctors and<br>Medical Providers that Provide Services on a Lien or Letter of Protection.</h1>

<!-- search -->
<div class="abs search-panel"></div>
<div class="abs panel-divider"></div>
<div class="abs panel-title" style="left:248px;top:325px">Quick Search for a Medical Provider by Category and/or Location</div>
<div class="abs field" style="left:232px;top:351px;width:480px;height:48px">Input Medical Provider Category or Name and City, State or Zip Code</div>
<div class="abs search-btn" style="left:664px;top:359px;width:40px;height:32px;background:var(--brand-blue)">
  <svg width="18" height="18" viewBox="0 0 18 18"><circle cx="7.5" cy="7.5" r="5.5" stroke="#fff" stroke-width="2.2" fill="none"/><path d="M11.5 11.5l5 5" stroke="#fff" stroke-width="2.6"/></svg>
</div>

<div class="abs panel-title" style="left:248px;top:428px">Advanced Search</div>
<div class="abs field" style="left:232px;top:456px;width:480px;height:30px">Provider Category<span class="caret">▼</span></div>
<div class="abs field" style="left:232px;top:504px;width:232px;height:30px">Address</div>
<div class="abs field" style="left:480px;top:504px;width:232px;height:30px">City</div>
<div class="abs field" style="left:232px;top:552px;width:232px;height:30px">State</div>
<div class="abs field" style="left:480px;top:552px;width:168px;height:30px">Zip</div>
<div class="abs search-btn" style="left:664px;top:551px;width:40px;height:32px;background:#c4c4c4">
  <svg width="18" height="18" viewBox="0 0 18 18"><circle cx="7.5" cy="7.5" r="5.5" stroke="#1f62ab" stroke-width="2.2" fill="none"/><path d="M11.5 11.5l5 5" stroke="#1f62ab" stroke-width="2.6"/></svg>
</div>
<div class="abs field" style="left:232px;top:600px;width:480px;height:30px">Screen by Medical Provider Network<span class="caret">▼</span></div>

<!-- how to -->
<div class="abs howto"></div>
<div class="abs howto-title" style="left:753px;top:325px">How to Use TrevaloCare.com</div>
<p class="abs howto-text" style="left:753px;top:350px">Quickly search for a Medical Provider by entering a City Name or Zip Code. You may include a Provider Category like 'Chiropractor' to just show that type of Provider</p>
<div class="abs howto-rule"></div>
<p class="abs howto-text" style="left:753px;top:416px">Use the Advanced Search to input a specific address, choose a Provider Category, and optionally screen results by members of a Medical Provider Network for Worker's Compensation cases.</p>
<span class="abs read-more">Read more &gt;</span>
<div class="abs howto-title" style="left:753px;top:503px">Video Explaining<br>TrevaloCare.com</div>
<div class="abs video" role="img" aria-label="Introduction video player placeholder"></div>
<span class="abs video-brand">vidmora</span>
<div class="abs video-bar"></div>
<div class="abs video-progress"></div>
<div class="abs video-progress-played"></div>

<!-- footer -->
<span class="abs footer-link" style="left:223px">Home</span>
<span class="abs footer-link" style="left:278px">About Us</span>
<span class="abs footer-link" style="left:348px">Attorney Information</span>
<span class="abs footer-link footer-cta" style="left:477px"><span class="star" style="font-size:10px;top:-6px;left:-8px">*</span>Medical Providers - List Your Office <span class="free">for Free!</span></span>
<span class="abs footer-link" style="left:847px;top:738px;color:#444">Privacy Policy</span>
<span class="abs footer-link" style="left:929px;top:738px">Contact Us</span>
<div class="abs footer-rule"></div>
<div class="abs footer-active"></div>

</body>
</html>
```